KORVELTA Corporate Business Card

Modern business card design for company which focuses in the areas of Staffing, IT Consulting & Data Services. Please note: We are no longer using the IT subscript on the logo. All designs should have IT subscript removed.
Website: www.korveltait.example

```html
<!DOCTYPE html>
<html lang="en">
<head>
<meta charset="utf-8">
<title>KORVELTA Business Card</title>
<link rel="stylesheet" href="https://fonts.googleapis.com/css2?family=Lato:wght@300;400;700;900&display=swap">
<style>
  :root {
    --page-bg: #e9ecef;
    --navy-light: #16305a;
    --navy-dark: #0c1829;
    --brand-blue: #1f8fd6;
    --brand-blue-deep: #1466b8;
    --brand-blue-pale: #a9d6f3;
    --paper: #ffffff;
    --ink: #1b1b1b;
    --ink-soft: #333a40;
  }
  * { box-sizing: border-box; margin: 0; padding: 0; }
  html, body {
    width: 1200px; height: 900px; overflow: hidden;
    background: var(--page-bg);
    font-family: "Lato", sans-serif;
  }
  .canvas {
    width: 1200px; height: 900px;
    display: flex; align-items: center; justify-content: center; gap: 36px;
  }
  .card {
    position: relative;
    width: 560px; height: 320px;
    overflow: hidden;
    box-shadow: 0 10px 28px rgba(0,0,0,.18);
  }

  /* front */
  .card--front {
    background: radial-gradient(ellipse at 40% 30%, var(--navy-light) 0%, var(--navy-dark) 85%);
  }
  .pixel-field {
    position: absolute; top: 0; height: 100%;
  }
  .pixel-field--left  { left: 0; width: 130px; }
  .pixel-field--right { right: 0; width: 130px; }
  .card--front .pixel-field--left {
    background: linear-gradient(90deg, var(--brand-blue-deep) 0%, rgba(31,143,214,.55) 55%, rgba(31,143,214,0) 100%);
    clip-path: polygon(0 0, 55% 0, 100% 100%, 0 100%);
  }
  .card--front .pixel-field--right {
    background: linear-gradient(270deg, var(--brand-blue-deep) 0%, rgba(31,143,214,.55) 55%, rgba(31,143,214,0) 100%);
    clip-path: polygon(0 0, 100% 0, 100% 100%, 45% 100%);
  }
  .wordmark {
    font-weight: 700;
    letter-spacing: 3px;
    display: flex; align-items: center; gap: 10px;
  }
  .wordmark__square { width: 16px; height: 16px; display: block; }
  .card--front .wordmark {
    position: absolute; left: 50%; top: 50%;
    transform: translate(-50%, -50%);
    font-size: 46px; color: #ffffff;
  }
  .card--front .wordmark__square { background: #ffffff; }

  /* back */
  .card--back { background: var(--paper); }
  .card--back .pixel-field--left {
    background: linear-gradient(90deg, var(--brand-blue) 0%, rgba(169,214,243,.7) 55%, rgba(169,214,243,0) 100%);
    clip-path: polygon(0 20%, 60% 0, 100% 100%, 0 100%);
  }
  .card--back .pixel-field--right {
    background: linear-gradient(270deg, var(--brand-blue-deep) 0%, rgba(169,214,243,.7) 55%, rgba(169,214,243,0) 100%);
    clip-path: polygon(20% 0, 100% 0, 100% 80%, 40% 100%);
  }
  .contact-panel {
    position: absolute; left: 170px; top: 30px;
    width: 270px; padding: 0 0 16px 0;
    border-bottom: 1px solid rgba(0,0,0,.06);
    box-shadow: 0 8px 10px -10px rgba(0,0,0,.25);
  }
  .contact-panel__name {
    font-size: 20px; font-weight: 900; color: var(--ink); letter-spacing: .5px;
  }
  .contact-panel__name span { font-weight: 300; color: var(--brand-blue); }
  .contact-panel__role {
    font-size: 12px; font-weight: 300; color: var(--brand-blue); margin-bottom: 10px;
  }
  .contact-panel__address {
    font-size: 11.5px; color: var(--ink-soft); line-height: 1.35; margin-bottom: 8px;
  }
  .contact-list { list-style: none; }
  .contact-list li {
    display: flex; align-items: center; gap: 7px;
    font-size: 11.5px; color: var(--ink-soft); line-height: 1.55;
  }
  .contact-list svg { width: 11px; height: 11px; flex: none; }
  .card--back .wordmark {
    position: absolute; left: 175px; bottom: 52px;
    font-size: 40px; color: var(--brand-blue);
  }
  .card--back .wordmark__square { background: var(--brand-blue); }
</style>
</head>
<body>
<main class="canvas">

  <section class="card card--front" aria-label="Business card front">
    <div class="pixel-field pixel-field--left" role="img" aria-label="Scattered blue pixel squares pattern"></div>
    <div class="pixel-field pixel-field--right" role="img" aria-label="Scattered blue pixel squares pattern"></div>
    <div class="wordmark"><i class="wordmark__square"></i>KORVELTA</div>
  </section>

  <section class="card card--back" aria-label="Business card back">
    <div class="pixel-field pixel-field--left" role="img" aria-label="Scattered blue pixel squares pattern"></div>
    <div class="pixel-field pixel-field--right" role="img" aria-label="Scattered blue pixel squares pattern"></div>

    <div class="contact-panel">
      <h1 class="contact-panel__name">DARIEN <span>HOLLOWAY</span></h1>
      <p class="contact-panel__role">Solution Manager</p>
      <p class="contact-panel__address">418 Ardent Lane<br>Millbrook, ST 00000</p>
      <ul class="contact-list">
        <li>
          <svg viewBox="0 0 12 12" aria-hidden="true"><path d="M2 1h2.5l1 3-1.5 1a6 6 0 0 0 3 3l1-1.5 3 1V10a1 1 0 0 1-1 1A9 9 0 0 1 1 2a1 1 0 0 1 1-1z" fill="var(--brand-blue)"/></svg>
          555-014-2290
        </li>
        <li>
          <svg viewBox="0 0 12 12" aria-hidden="true"><circle cx="6" cy="6" r="5" fill="none" stroke="var(--brand-blue)" stroke-width="1.2"/><path d="M6 3v3l2 1.5" fill="none" stroke="var(--brand-blue)" stroke-width="1.2"/></svg>
          Monday-Friday (8am-5pm EST)
        </li>
        <li>
          <svg viewBox="0 0 12 12" aria-hidden="true"><rect x="1" y="2.5" width="10" height="7" fill="var(--brand-blue)"/><path d="M1 2.5l5 4 5-4" fill="none" stroke="#fff" stroke-width="1"/></svg>
          contactus@korveltait.example
        </li>
        <li>
          <svg viewBox="0 0 12 12" aria-hidden="true"><circle cx="6" cy="6" r="5" fill="var(--brand-blue)"/><path d="M1 6h10M6 1c-2.5 3-2.5 7 0 10M6 1c2.5 3 2.5 7 0 10" fill="none" stroke="#fff" stroke-width=".8"/></svg>
          www.korveltait.example
        </li>
      </ul>
    </div>

    <div class="wordmark"><i class="wordmark__square"></i>KORVELTA</div>
  </section>

</main>
</body>
</html>
```